car wrap design 2019 Korvane 170WB high roof white color

Im looking for a catchy but simple car wrap design for a van 2019Mercedes Korvane Van 170 WB . Its a Heating and Cooling company specializing in the residential market. Installation, service and maintenance of all heating and Cooling equipment . Van is white and im looking for a partial wrap with 3 other colours red ,blue and grey. Something simple my name "The Brindlow Heating and Cooling " website "thebrindlow.ca phone nr "555-310-4826 and logo and description of what im doing . .

Industry/Entity Type

Hvac

Colors

Designer to choose colors to be used in the design.

Requirements
Must have
• big logo see file attached phone nr 555-310-4826 web. thebrindlow.ca
Nice to have
• stand out logo visible ,phone nr
Should not have
• too many colours max 4 colours white red blue and maybe gray. no curvy lines

```html
<!DOCTYPE html>
<html lang="en">
<head>
<meta charset="utf-8">
<title>The Brindlow Heating and Cooling — Korvane van wrap</title>
<link rel="stylesheet" href="https://fonts.googleapis.com/css2?family=Open+Sans:wght@400;700;800&family=Oswald:wght@500;600&display=swap">
<style>
  :root {
    --page: #eceef0;
    --wrap-orange: #e8501c;
    --wrap-red: #c8151d;
    --wrap-blue: #1b9ad9;
    --wrap-navy: #0d3866;
    --wrap-grey: #c9ccd0;
    --wrap-white: #ffffff;
    --band-dark: #1a0a0a;
    --glass: #2b2f33;
    --tyre: #2a2a2a;
  }
  html, body { margin: 0; padding: 0; overflow: hidden; }
  body { width: 1200px; height: 901px; background: var(--page); }
  .van-wrap { display: block; width: 1200px; height: 901px; }
  .heading { font-family: "Open Sans", sans-serif; font-weight: 700; fill: var(--wrap-white); }
  .service-list { font-family: "Open Sans", sans-serif; font-weight: 700; fill: var(--wrap-white); font-size: 15px; }
  .phone { font-family: "Oswald", sans-serif; font-weight: 600; fill: var(--wrap-white); font-size: 36px; }
  .website { font-family: "Open Sans", sans-serif; font-weight: 400; fill: var(--wrap-white); font-size: 18px; }
  .website-strong { font-weight: 700; }
  .hours-big { font-family: "Oswald", sans-serif; font-weight: 600; fill: var(--wrap-white); font-size: 40px; }
  .hours-small { font-family: "Open Sans", sans-serif; font-weight: 700; fill: var(--wrap-white); font-size: 16px; }
  .brand-name { font-family: "Open Sans", sans-serif; font-weight: 800; fill: var(--wrap-red); }
  .tagline-install { font-family: "Oswald", sans-serif; font-weight: 600; fill: var(--wrap-navy); font-size: 44px; }
  .tagline-maint { font-family: "Oswald", sans-serif; font-weight: 600; fill: var(--wrap-orange); font-size: 44px; }
  .tagline-sub { font-family: "Open Sans", sans-serif; font-weight: 400; fill: #555; font-size: 9.5px; }
</style>
</head>
<body>
<svg class="van-wrap" viewBox="0 0 1200 901" xmlns="http://www.w3.org/2000/svg">
  <defs>
    <linearGradient id="redSide" x1="0" y1="0" x2="1" y2="0">
      <stop offset="0" stop-color="var(--wrap-orange)"/>
      <stop offset="0.45" stop-color="#dc3a1c"/>
      <stop offset="1" stop-color="var(--wrap-red)"/>
    </linearGradient>
    <linearGradient id="unitFill" x1="0" y1="0" x2="1" y2="0">
      <stop offset="0" stop-color="#b9bcbf"/>
      <stop offset="1" stop-color="#8e9296"/>
    </linearGradient>
    <clipPath id="vanBody">
      <path d="M20 540 L20 455 Q24 418 60 408 L120 395 Q150 380 190 320 L260 215 Q300 175 370 170 L1120 170 Q1140 175 1145 210 L1152 540 Z"/>
    </clipPath>
  </defs>

  <!-- van body panels -->
  <g class="body-panels" clip-path="url(#vanBody)">
    <rect class="panel-white" x="0" y="150" width="1200" height="420" fill="var(--wrap-white)"/>
    <polygon class="panel-red" points="0,150 672,150 685,420 570,560 0,560" fill="url(#redSide)"/>
    <polygon class="panel-grey" points="600,470 650,470 612,560 570,560" fill="var(--wrap-grey)"/>
    <polygon class="panel-blue" points="1063,170 1200,170 1200,560 615,560" fill="var(--wrap-blue)"/>
    <line class="pinstripe-blue" x1="1040" y1="172" x2="880" y2="380" stroke="var(--wrap-blue)" stroke-width="1.5"/>
    <ellipse class="brand-circle" cx="800" cy="282" rx="170" ry="167" fill="var(--wrap-white)"/>
    <ellipse class="brand-ring" cx="800" cy="280" rx="155" ry="152" fill="none" stroke="var(--wrap-blue)" stroke-width="1.2"/>
    <rect class="lower-band" x="0" y="470" width="1200" height="36" fill="var(--band-dark)" opacity="0.55"/>
    <path class="service-swoosh" d="M345 170 Q335 215 345 245 Q360 330 400 365 Q470 405 560 375 Q610 345 632 300" fill="none" stroke="var(--wrap-white)" stroke-width="3"/>
  </g>

  <!-- cab glass and wheels -->
  <polygon class="cab-window" points="179,380 262,262 385,250 376,336 288,374" fill="var(--glass)"/>
  <circle class="wheel" cx="165" cy="548" r="58" fill="var(--tyre)"/>
  <circle class="wheel" cx="895" cy="558" r="58" fill="var(--tyre)"/>

  <!-- services -->
  <text class="heading" x="425" y="222" font-size="26">WHAT WE DO</text>
  <g class="service-list">
    <circle cx="433" cy="252" r="3.5" fill="#fff"/><text x="448" y="258">FURNACE</text>
    <circle cx="433" cy="273" r="3.5" fill="#fff"/><text x="448" y="279">AIR CONDITIONING</text>
    <circle cx="433" cy="294" r="3.5" fill="#fff"/><text x="448" y="300">WATER HEATERS</text>
    <circle cx="433" cy="314" r="3.5" fill="#fff"/><text x="448" y="320">FIRE PLACES</text>
    <circle cx="433" cy="335" r="3.5" fill="#fff"/><text x="448" y="341">GAS LINES</text>
    <circle cx="433" cy="355" r="3.5" fill="#fff"/><text x="448" y="361">HUMIDIFIERS</text>
  </g>

  <!-- contact -->
  <g class="phone-icon" fill="none" stroke="#fff" stroke-width="2.4" stroke-linecap="round">
    <path d="M422 412 q-4 8 6 16 q8 6 13 1 l-4 -4 q-3 2 -6 -1 q-4 -4 -1 -7 l-4 -5 z" fill="#fff"/>
    <path d="M436 410 q6 1 7 7"/>
  </g>
  <text class="phone" x="447" y="436" textLength="190" lengthAdjust="spacingAndGlyphs">555-310-4826</text>
  <circle class="web-icon" cx="430" cy="451" r="9" fill="none" stroke="#fff" stroke-width="1.6"/>
  <text class="website" x="445" y="458" textLength="193" lengthAdjust="spacingAndGlyphs">www.<tspan class="website-strong">thebrindlow</tspan>.ca</text>

  <text class="hours-big" x="230" y="452">24/7</text>
  <text class="hours-small" x="310" y="441">HOUR</text>
  <text class="hours-small" x="310" y="457">SERVICE</text>

  <!-- brand -->
  <circle class="brand-dot" cx="808" cy="212" r="18" fill="var(--wrap-red)"/>
  <text class="brand-name" x="810" y="265" font-size="30" text-anchor="middle" textLength="262" lengthAdjust="spacingAndGlyphs">THE BRINDLOW</text>
  <text class="brand-name" x="810" y="287" font-size="14" text-anchor="middle" textLength="255" lengthAdjust="spacingAndGlyphs">HEATING AND COOLING</text>
  <text class="tagline-install" x="693" y="342" textLength="199" lengthAdjust="spacingAndGlyphs">INSTALLATION</text>
  <text class="tagline-maint" x="693" y="382" textLength="199" lengthAdjust="spacingAndGlyphs">MAINTENANCE</text>
  <text class="tagline-sub" x="694" y="395" textLength="193" lengthAdjust="spacingAndGlyphs">OF ALL HEATING AND COOLING EQUIPMENT</text>

  <rect class="condenser-unit" x="950" y="270" width="158" height="196" rx="4" fill="url(#unitFill)" role="img" aria-label="Outdoor air conditioning condenser unit"/>
</svg>
</body>
</html>
```